Tending Our Garden eBook Cover Design

I want to deisgn a cover for my eBook (FRONT COVER) and the title is:

What I Grew From a Single Spark. And Why It Matters
By KT Dorran

TITLE CHANGED TO: UNDER THE WILLOW TREE; WHERE I FOUND MY QUIET STRENGTH AND WHERE YOU MIGHT TOO

The color palette is attached. Along with some photos options of me. Along with the ebook in WORD Document. My website is www.KTDorranLive.example. You can use a different color palette if you think it is best

Target Market(s)

women who look to build a personal brand

Industry/Entity Type

health and wellness

Requirements
Must have
• the title
Nice to have
• use my picture on the cover; but that is optional
Should not have
• any men

```html
<!DOCTYPE html>
<html lang="en">
<head>
<meta charset="utf-8">
<title>Under the Willow Tree — KT Dorran</title>
<link rel="stylesheet" href="https://fonts.googleapis.com/css2?family=Montserrat:wght@800;900&display=swap">
<style>
  :root {
    --stage: #e9e9e9;
    --rose: #ec4f80;
    --rose-deep: #e8457a;
    --rose-soft: #f6c3d4;
    --title-pink: #ee6e95;
    --paper: #ffffff;
    --ink: #111111;
    --dress-red: #e8262a;
    --hair: #2a1f1f;
  }
  * { box-sizing: border-box; margin: 0; padding: 0; }
  html, body {
    width: 1200px;
    height: 768px;
    overflow: hidden;
    background: var(--stage);
  }
  .stage {
    position: relative;
    width: 1200px;
    height: 768px;
  }
  .cover {
    position: absolute;
    left: 390px;
    top: 68px;
    width: 420px;
    height: 632px;
    background: var(--paper);
    overflow: hidden;
    font-family: "Montserrat", Arial, sans-serif;
  }
  .cover__topbar {
    position: absolute;
    left: 0; top: 0;
    width: 100%;
    height: 19px;
    background: var(--rose);
  }
  .cover__header {
    position: absolute;
    left: 0; top: 19px;
    width: 100%;
    height: 191px;
    padding: 0 12px;
    display: flex;
    flex-direction: column;
    justify-content: center;
    gap: 14px;
    color: var(--title-pink);
    font-weight: 900;
    text-transform: uppercase;
    line-height: 1;
  }
  .cover__header span {
    display: block;
    white-space: nowrap;
    letter-spacing: -0.5px;
  }
  .cover__header .line-1 { font-size: 35px; }
  .cover__header .line-2 { font-size: 32px; }
  .cover__header .line-3 { font-size: 34px; }
  .cover__panel {
    position: absolute;
    left: 0; top: 210px;
    width: 100%;
    height: 422px;
    background: linear-gradient(180deg, var(--rose-deep) 0%, var(--rose-soft) 45%, var(--rose-soft) 60%, var(--rose-deep) 100%);
  }
  .cover__portrait {
    position: absolute;
    left: 190px;
    top: 196px;
    width: 230px;
    height: 436px;
    border-radius: 100px 100px 0 0;
    background: linear-gradient(180deg, var(--hair) 0%, #4a2e28 30%, var(--dress-red) 46%, var(--dress-red) 100%);
  }
  .cover__subtitle {
    position: absolute;
    left: 12px;
    top: 214px;
    color: var(--paper);
    font-weight: 900;
    text-transform: uppercase;
    font-size: 66px;
    line-height: 80px;
    letter-spacing: -1px;
  }
  .cover__subtitle span { display: block; white-space: nowrap; }
  .cover__author {
    position: absolute;
    right: 44px;
    bottom: 16px;
    color: var(--ink);
    font-weight: 800;
    font-size: 17px;
  }
</style>
</head>
<body>
  <main class="stage">
    <article class="cover">
      <div class="cover__topbar"></div>
      <h1 class="cover__header">
        <span class="line-1">Under the Willow</span>
        <span class="line-2">Tree; Where I Found</span>
        <span class="line-3">My Quiet Strength</span>
      </h1>
      <div class="cover__panel"></div>
      <div class="cover__portrait" role="img" aria-label="Portrait photo of the author with long dark hair and a red top"></div>
      <p class="cover__subtitle">
        <span>And</span>
        <span>Where</span>
        <span>You</span>
        <span>Might</span>
        <span>Too</span>
      </p>
      <p class="cover__author">KT Dorran</p>
    </article>
  </main>
</body>
</html>
```